Varno - Company: Varno Immobilien *

Design of a company logo and business card layout

A real estate managment start up for propertiy managing based in Switzerland.

Porperty management for private and institutional clients in Europe.

Digitalization is the key driver of the business. The company offers digital way of managing properties, handling clients and tenants as well as reporting.

By using digital tools for mangement and reporting the clients will have much more transparency an access to their properies and details.

The company wants to be one of the driving forces of proptech (property and Tech) in the industry.

Target Market(s)

Private Real Estate owners under 50 years of age with minimum portfolio of 20 units.
Smaler instiutional real estate owners including but not limited to pension funds, insurance companies etc.

Industry/Entity Type

Real Estate

Contact Information for Business Card

Words in parentheses only for you information, not for business card design

"Company name:" Varno Immobilien GmbH
"Name:" Dr. Ole Brust
"Position:" Geschäftsführer
"Address:" Wiesmattweg 17, CH-8047 Zürich
"E-mail:" ole.brust@varno-immobilien-beispiel.ch
"Phone:" +41-79-804.27.15

Number of Pages Required

1 page

Font styles to use
Serif

Colors

Designer to choose colors to be used in the design.

Requirements
Must have
• 1. A logo "Varno Immobilien"
• 2. A matching symbol (logo can be used with or without symbol)
• 3. A tagline: "digital und transparent"
• 4. Connection to Digitalzation and Transparency
• !!! the uploaded file is JUST an EXEMPLE, do not include in the logo !!!
• No swiss Flag or Cross
• No mountains or landscape
• No Dollar or Swiss Franks notes
Should not have
• Old school design
• To much Swissness
• No sweet colors like pink

```html
<!DOCTYPE html>
<html lang="de">
<head>
<meta charset="utf-8">
<title>Varno Immobilien – Logo und Visitenkarte</title>
<link rel="stylesheet" href="https://fonts.googleapis.com/css2?family=Questrial&family=Saira+Semi+Condensed:wght@400&display=swap">
<style>
  :root {
    --brand-red: #8a161a;
    --ink: #23242c;
    --muted: #6b6b70;
    --paper: #ffffff;
    --backdrop: #e6e6ea;
  }
  * { margin: 0; padding: 0; box-sizing: border-box; }
  html, body { width: 1200px; height: 830px; overflow: hidden; }
  body {
    background: var(--backdrop);
    position: relative;
    font-family: "Questrial", sans-serif;
    color: var(--ink);
  }
  .card {
    position: absolute;
    width: 534px;
    height: 312px;
  }
  .card--front { left: 126px; top: 112px; background: var(--paper); }
  .card--back { left: 387px; top: 439px; background: var(--brand-red); color: var(--paper); }

  .brand {
    position: absolute;
    display: flex;
    flex-direction: column;
    align-items: center;
    text-align: center;
  }
  .brand__mark {
    width: 62px; height: 62px;
    background: var(--brand-red);
    margin-bottom: 30px;
  }
  .brand__name {
    font-family: "Questrial", sans-serif;
    font-size: 22px;
    letter-spacing: 1.5px;
    text-transform: uppercase;
    color: var(--ink);
    white-space: nowrap;
  }
  .brand__tagline {
    font-family: "Saira Semi Condensed", sans-serif;
    font-size: 14px;
    color: var(--brand-red);
    margin-top: 2px;
  }

  .card--front .brand { left: 20px; width: 250px; top: 72px; }

  .contact { position: absolute; left: 281px; top: 64px; }
  .contact__name { font-size: 26px; line-height: 1; letter-spacing: 0.3px; }
  .contact__role { font-family: Arial, sans-serif; font-size: 12px; color: var(--muted); margin-top: 3px; }
  .contact__list { list-style: none; margin-top: 26px; }
  .contact__item {
    display: flex; align-items: flex-start;
    font-size: 12.5px; line-height: 18px; margin-bottom: 3px; letter-spacing: 0.3px;
  }
  .contact__item--phone { font-size: 14px; margin-bottom: 6px; }
  .contact__icon { width: 12px; height: 12px; margin: 3px 15px 0 0; flex: none; fill: var(--brand-red); }

  .card--back .brand { left: 0; width: 100%; top: 56px; }
  .card--back .brand__mark { width: 80px; height: 80px; background: var(--paper); margin-bottom: 44px; }
  .card--back .brand__name { color: var(--paper); font-size: 27px; letter-spacing: 2px; }
  .card--back .brand__tagline { color: var(--paper); font-size: 15px; }
  .card__url {
    position: absolute; left: 0; width: 100%; top: 269px;
    text-align: center; font-size: 16px; letter-spacing: 0.8px;
  }

  .logo-lockup { left: 740px; width: 380px; top: 130px; }
  .logo-lockup .brand__mark { width: 120px; height: 120px; margin-bottom: 44px; }
  .logo-lockup .brand__name { font-size: 33px; letter-spacing: 2.5px; }
  .logo-lockup .brand__tagline { font-size: 20px; margin-top: 2px; }
</style>
</head>
<body>
  <section class="card card--front">
    <div class="brand">
      <div class="brand__mark"></div>
      <div class="brand__name">Varno Immobilien</div>
      <div class="brand__tagline">digital und transparent</div>
    </div>
    <div class="contact">
      <div class="contact__name">Dr. Ole Brust</div>
      <div class="contact__role">Geschäftsführer</div>
      <ul class="contact__list">
        <li class="contact__item contact__item--phone">
          <svg class="contact__icon" viewBox="0 0 24 24"><path d="M6.6 10.8a15 15 0 0 0 6.6 6.6l2.2-2.2c.3-.3.7-.4 1-.2 1.1.4 2.3.6 3.6.6.6 0 1 .4 1 1V20c0 .6-.4 1-1 1A17 17 0 0 1 3 4c0-.6.4-1 1-1h3.5c.6 0 1 .4 1 1 0 1.3.2 2.5.6 3.6.1.3 0 .7-.2 1z"/></svg>
          +41-79-804.27.15
        </li>
        <li class="contact__item">
          <svg class="contact__icon" viewBox="0 0 24 24"><path d="M2 5h20v14H2z M3.5 6.5 12 13l8.5-6.5" fill="none" stroke="var(--brand-red)" stroke-width="2.4"/></svg>
          ole.brust@varno-immobilien-beispiel.ch
        </li>
        <li class="contact__item">
          <svg class="contact__icon" viewBox="0 0 24 24"><circle cx="12" cy="12" r="10"/><path d="M7 6c2 1 2 3 4 3s1 3 3 3-1 4 1 6" fill="none" stroke="#fff" stroke-width="2"/></svg>
          www.varno-immobilien-beispiel.ch
        </li>
        <li class="contact__item">
          <svg class="contact__icon" viewBox="0 0 24 24"><path d="M12 2a7 7 0 0 0-7 7c0 5 7 13 7 13s7-8 7-13a7 7 0 0 0-7-7zm0 9.5A2.5 2.5 0 1 1 12 6.5a2.5 2.5 0 0 1 0 5z"/></svg>
          <span>Varno Immobilien GmbH<br>Wiesmattweg 17<br>CH-8047 Zürich</span>
        </li>
      </ul>
    </div>
  </section>

  <section class="brand logo-lockup">
    <div class="brand__mark"></div>
    <div class="brand__name">Varno Immobilien</div>
    <div class="brand__tagline">digital und transparent</div>
  </section>

  <section class="card card--back">
    <div class="brand">
      <div class="brand__mark"></div>
      <div class="brand__name">Varno Immobilien</div>
      <div class="brand__tagline">digital und transparent</div>
    </div>
    <div class="card__url">www.varno-immobilien-beispiel.ch</div>
  </section>
</body>
</html>
```